Engineering firm Hero image for new web page

We are building a new webpage and need a Hero image. I have included a screen grab of the landing page showing where the image will be located. The company tag line (Engineering Tomorrow’s Automation) will be overlaid on the image so we need to be sure it works with the overlay.
We service a number of different industries, and we want something that is not overly specific so that if potential customers see something they don't recognize that we don't run them off. I have found several examples of a style that I think will work very well for us.
I want the Hero image to incorporate our competencies: Engineering, Automation, Integration, Robotics, Controls, Optimization.
There will be a follow on project to create a second image in the same theme which will highlight our industries served. Those will be: Food processing, Oil & Gas, Automotive, Aerospace, Medical, Contract Manufacturing. This image will be just below the hero and will be part of the “who we are section”

```html
<!DOCTYPE html>
<html lang="en">
<head>
<meta charset="utf-8">
<title>Hero Image – Engineering Tomorrow's Automation</title>
<link href="https://fonts.googleapis.com/css2?family=Poppins:wght@700&family=Orbitron:wght@500;700&display=swap" rel="stylesheet">
<style>
  :root {
    --page-bg: #ffffff;
    --heading: #1f0b0b;
    --banner-deep: #050203;
    --banner-red: #8a0a10;
    --banner-wine: #3a0509;
    --accent: #ff2a1a;
    --accent-soft: #ff6a55;
    --ring-fill: #5a0a0e;
    --label: #ffffff;
  }
  * { margin: 0; padding: 0; box-sizing: border-box; }
  html, body {
    width: 1200px; height: 800px; overflow: hidden;
    background: var(--page-bg);
  }
  .board { position: relative; width: 1200px; height: 800px; }
  .board-title {
    position: absolute; top: 170px; left: 0; width: 100%;
    text-align: center;
    font-family: "Poppins", sans-serif; font-weight: 700;
    font-size: 24px; color: var(--heading); letter-spacing: 0.3px;
  }
  .hero-banner {
    position: absolute; left: 218px; top: 258px;
    width: 772px; height: 290px; overflow: hidden;
    background: linear-gradient(90deg, var(--banner-red) 0%, var(--banner-wine) 45%, var(--banner-deep) 100%);
  }
  .hero-banner svg { display: block; width: 100%; height: 100%; }
  .hero-hand {
    position: absolute; left: 0; top: 70px; width: 330px; height: 220px;
    background: radial-gradient(ellipse at 45% 55%, #c46a55 0%, #9a3a2e 35%, rgba(140,20,20,0.5) 65%, rgba(120,10,15,0) 80%);
  }
  .tagline, .competency-label, .industry-label {
    font-family: "Orbitron", sans-serif; fill: var(--label);
  }
  .tagline { font-size: 13px; font-weight: 700; letter-spacing: 0.2px; }
  .competency-label { font-size: 7.8px; font-weight: 700; }
  .industry-label { font-size: 6px; font-weight: 500; }
  .node-ring { fill: var(--ring-fill); stroke: var(--accent); stroke-width: 1.6; }
  .node-icon { fill: none; stroke: var(--accent-soft); stroke-width: 1; }
</style>
</head>
<body>
<div class="board">
  <h1 class="board-title">HERO IMAGE</h1>

  <div class="hero-banner">
    <div class="hero-hand" role="img" aria-label="Photo of a reaching hand pointing toward the central tagline circle"></div>
    <svg viewBox="0 0 772 290" aria-label="Competencies and industries served">
      <defs>
        <radialGradient id="coreFill" cx="50%" cy="40%" r="60%">
          <stop offset="0%" stop-color="#8c1410"/>
          <stop offset="100%" stop-color="#3d0507"/>
        </radialGradient>
        <radialGradient id="nodeFill" cx="40%" cy="35%" r="70%">
          <stop offset="0%" stop-color="#6e0d10"/>
          <stop offset="100%" stop-color="#2a0406"/>
        </radialGradient>
        <g id="gear-icon">
          <circle r="5" class="node-icon"/>
          <circle r="2" class="node-icon"/>
          <path class="node-icon" d="M0-8V-6M0 6V8M-8 0H-6M6 0H8M-5.7-5.7L-4.2-4.2M4.2 4.2L5.7 5.7M-5.7 5.7L-4.2 4.2M4.2-4.2L5.7-5.7"/>
        </g>
      </defs>

      <!-- Tagline core -->
      <g class="core">
        <circle cx="385" cy="116" r="74" fill="url(#coreFill)"/>
        <path d="M395 43 A74 74 0 0 1 436 170" fill="none" stroke="var(--accent)" stroke-width="4"/>
        <path d="M436 170 A74 74 0 0 1 418 182" fill="none" stroke="#ffffff" stroke-width="3"/>
        <path d="M313 70 A74 74 0 0 0 375 190" fill="none" stroke="var(--accent)" stroke-width="2.5"/>
        <text class="tagline" x="385" y="88" text-anchor="middle">ENGINEERING</text>
        <text class="tagline" x="385" y="104" text-anchor="middle">TOMORROW'S</text>
        <text class="tagline" x="385" y="120" text-anchor="middle">AUTOMATION</text>
        <g transform="translate(385 150) scale(2.2)"><use href="#gear-icon"/></g>
      </g>

      <!-- Competencies -->
      <g class="competency">
        <circle class="node-ring" cx="470" cy="40" r="21" fill="url(#nodeFill)"/>
        <g transform="translate(470 40) scale(1.2)"><use href="#gear-icon"/></g>
        <text class="competency-label" x="502" y="38">CONTROLS</text>
      </g>
      <g class="competency">
        <circle class="node-ring" cx="501" cy="98" r="21" fill="url(#nodeFill)"/>
        <g transform="translate(501 98) scale(1.2)"><use href="#gear-icon"/></g>
        <text class="competency-label" x="532" y="100">ROBOTICS</text>
      </g>
      <g class="competency">
        <circle class="node-ring" cx="495" cy="159" r="21" fill="url(#nodeFill)"/>
        <g transform="translate(495 159) scale(1.2)"><use href="#gear-icon"/></g>
        <text class="competency-label" x="531" y="169">INTEGRATION</text>
      </g>
      <g class="competency">
        <circle class="node-ring" cx="449" cy="211" r="21" fill="url(#nodeFill)"/>
        <g transform="translate(449 211) scale(1.2)"><use href="#gear-icon"/></g>
        <text class="competency-label" x="490" y="215">AUTOMATION</text>
      </g>
      <g class="competency">
        <circle class="node-ring" cx="386" cy="234" r="30" fill="url(#nodeFill)"/>
        <g transform="translate(386 234) scale(1.6)"><use href="#gear-icon"/></g>
        <text class="competency-label" x="426" y="257">ENGINEERING</text>
      </g>

      <!-- Industries -->
      <g class="industry">
        <circle class="node-ring" cx="578" cy="18" r="16" fill="url(#nodeFill)"/>
        <g transform="translate(578 18) scale(0.9)"><use href="#gear-icon"/></g>
        <text class="industry-label" x="604" y="16">AUTOMOTIVE</text>
      </g>
      <g class="industry">
        <circle class="node-ring" cx="615" cy="61" r="16" fill="url(#nodeFill)"/>
        <g transform="translate(615 61) scale(0.9)"><use href="#gear-icon"/></g>
        <text class="industry-label" x="642" y="61">MEDICAL</text>
      </g>
      <g class="industry">
        <circle class="node-ring" cx="626" cy="113" r="16" fill="url(#nodeFill)"/>
        <g transform="translate(626 113) scale(0.9)"><use href="#gear-icon"/></g>
        <text class="industry-label" x="653" y="112">CONTRACT</text>
        <text class="industry-label" x="653" y="119">MANUFACTURING</text>
      </g>
      <g class="industry">
        <circle class="node-ring" cx="622" cy="171" r="16" fill="url(#nodeFill)"/>
        <g transform="translate(622 171) scale(0.9)"><use href="#gear-icon"/></g>
        <text class="industry-label" x="648" y="172">FOOD AND</text>
        <text class="industry-label" x="648" y="179">BEVERAGE</text>
      </g>
      <g class="industry">
        <circle class="node-ring" cx="575" cy="215" r="16" fill="url(#nodeFill)"/>
        <g transform="translate(575 215) scale(0.9)"><use href="#gear-icon"/></g>
        <text class="industry-label" x="601" y="217">AEROSPACE</text>
      </g>
      <g class="industry">
        <circle class="node-ring" cx="526" cy="262" r="18" fill="url(#nodeFill)"/>
        <g transform="translate(526 262) scale(0.9)"><use href="#gear-icon"/></g>
        <text class="industry-label" x="555" y="264">OIL &amp; GAS</text>
      </g>
    </svg>
  </div>
</div>
</body>
</html>
```